Ridgecrest Balusters Website Redesign

I want a fresh new design for my website. Original website
www.ridgecrestbalusters.example. Will need to add additional photos for winning designer. Please use the basic layout for new design. Looking to get a more modern, functional site to attract new customer and ne bale to highlight past projects. Need it to be easy to navigate and get in touch with me for inquiries.

Target Market(s)

Builders and home owners in WA state

Industry/Entity Type

Building, Construction, Deck building

Coding

Coded - Design and coding required

Number of Pages Required

5+ page

Font styles to use
Sans Serif

Colors
0054AA
0677BA
7BADD7
CADEEF
E8F1F8
0094D4
00A9DD
6FCCEA
C7EBF8
E9F6FB
00AB8E
00BBA5
67D7C9
C6EFE9
E9F9F6
59FF00
82FF00
B8FF75
E3FFCB
F4FFEA

Requirements
Must have
• Will need to add more photos of completed projects
Nice to have
• Fresh take on old website, something modern
Should not have
• Nothing comes to mind

```html
<!DOCTYPE html>
<html lang="en">
<head>
<meta charset="utf-8">
<title>Ridgecrest Balusters</title>
<link href="https://fonts.googleapis.com/css2?family=Poppins:wght@400;500;600;700&display=swap" rel="stylesheet">
<style>
:root{
  --teal:#00ab8e;
  --teal-bright:#00bba5;
  --teal-soft:#67d7c9;
  --mint:#c6efe9;
  --mint-pale:#e9f9f6;
  --ink:#1f1f1f;
  --body:#333;
  --muted:#8a8a8a;
  --card:#f4f4f4;
  --line:#d6d6d6;
  --white:#fff;
}
*{box-sizing:border-box;margin:0;padding:0}
html,body{width:1200px;height:5337px;overflow:hidden}
body{font-family:'Poppins',sans-serif;color:var(--ink);background:var(--white);position:relative}
.btn{position:absolute;display:flex;align-items:center;justify-content:center;border-radius:20px;font-weight:600;font-size:13px;white-space:nowrap}
.btn-teal{background:var(--teal);color:var(--white)}
.btn-white{background:var(--white);color:var(--teal)}
.ph{position:absolute}

/* header */
.site-header{position:absolute;left:0;top:0;width:1200px;height:145px;background:var(--white)}
.brand{position:absolute;display:flex;align-items:center;gap:10px;font-weight:600;color:var(--teal);font-size:19px;line-height:1.15}
.brand .mark{width:14px;height:14px;background:var(--teal)}
.nav a{position:absolute;top:62px;font-size:14px;color:var(--ink);text-decoration:none}
.nav a.active{font-weight:600}
.nav a.active::after{content:"";position:absolute;left:0;right:0;bottom:-8px;height:4px;border-radius:2px;background:var(--teal)}
.phone-btn{left:972px;top:54px;width:163px;height:37px;gap:8px}

/* hero */
.hero{position:absolute;left:0;top:145px;width:1200px;height:555px;background:linear-gradient(100deg,#1a9e86 0%,#2fa58f 45%,#6a7d78 62%,#8a8e8a 100%)}
.hero-shadow{position:absolute;left:0;bottom:0;width:830px;height:190px;background:linear-gradient(180deg,rgba(0,0,0,0) 0%,rgba(20,30,28,.85) 80%)}
.hero h1{position:absolute;left:64px;top:70px;color:var(--ink);font-size:39px;font-weight:700;line-height:60px}
.hero p{position:absolute;left:64px;top:210px;width:430px;color:var(--white);font-size:14px;line-height:22px}
.hero .btn{left:64px;top:365px;width:143px;height:33px}

/* about */
.credentials{position:absolute;left:64px;top:770px;font-size:51px;font-weight:700;line-height:79px}
.credentials .accent{color:var(--teal)}
.about-label{position:absolute;left:584px;top:740px;font-size:37px;font-weight:600}
.about-title{position:absolute;left:584px;top:810px;font-size:38px;font-weight:700;color:var(--teal-bright);line-height:60px}
.about-copy{position:absolute;left:584px;top:942px;width:525px;font-size:14.2px;line-height:21.5px;color:var(--body)}

/* products */
.products{position:absolute;left:0;top:1310px;width:1200px;height:634px;background:var(--mint)}
.products-side{position:absolute;left:0;top:0;width:352px;height:634px;background:linear-gradient(160deg,#0fae93,#058a74);border-bottom-right-radius:130px}
.products-intro{position:absolute;left:390px;top:52px;width:410px;text-align:center;font-size:14px;line-height:23px}
.products h2{position:absolute;left:0;top:110px;width:1190px;text-align:center;font-size:38px;font-weight:700}
.product-card{position:absolute;top:186px;width:259px;height:358px;background:#f7f7f7;border-radius:6px;box-shadow:0 2px 8px rgba(0,0,0,.12)}
.product-card .ph{left:12px;top:12px;width:235px;height:164px}
.product-card h3{position:absolute;left:12px;top:196px;font-size:14px;font-weight:600;color:var(--teal-bright)}
.product-card p{position:absolute;left:12px;top:228px;width:232px;font-size:13.5px;line-height:21px}
.product-card .btn{left:12px;top:311px;width:122px;height:35px}
.dots{position:absolute;left:566px;top:590px;display:flex;gap:8px}
.dots span{width:8px;height:8px;border-radius:50%;background:#b7ddd6}
.dots span:first-child{background:var(--teal)}

/* why */
.why-title{position:absolute;left:64px;top:2005px;font-size:40px;font-weight:700;line-height:60px}
.feature{position:absolute;width:267px;height:308px;background:var(--teal);color:var(--white)}
.feature .num{position:absolute;left:16px;top:14px;font-size:38px;font-weight:700;color:#7fe0d0}
.feature h3{position:absolute;left:18px;top:72px;width:230px;font-size:18px;font-weight:600;line-height:29px}
.feature p{position:absolute;left:18px;width:235px;font-size:13.5px;line-height:21.5px}

/* process */
.process-title{position:absolute;left:0;top:2834px;width:1181px;text-align:center;font-size:39px;font-weight:700}
.process-card{position:absolute;top:2911px;width:340px;height:415px;background:var(--card);box-shadow:0 2px 8px rgba(0,0,0,.14)}
.process-card .ph{left:16px;top:16px;width:308px;height:191px}
.process-card .icon-box{position:absolute;left:248px;top:170px;width:78px;height:78px;background:var(--white);border-radius:6px;box-shadow:0 2px 6px rgba(0,0,0,.15);display:flex;align-items:center;justify-content:center}
.process-card h3{position:absolute;left:24px;top:250px;font-size:14px;font-weight:600;color:var(--teal)}
.process-card p{position:absolute;left:24px;top:278px;width:300px;font-size:13.5px;line-height:21px}
.process-card .btn{left:24px;top:357px;width:127px;height:33px}

/* service area */
.service{position:absolute;left:0;top:3384px;width:1200px;height:538px;background:linear-gradient(180deg,#90a7b0 0%,#6c7a70 40%,#3e4a3c 75%,#2a3428 100%)}
.service h2{position:absolute;left:58px;top:96px;color:var(--white);font-size:40px;font-weight:700;line-height:58px}
.service p{position:absolute;left:58px;top:226px;width:340px;color:var(--white);font-size:14px;line-height:21.5px}
.service .btn{left:58px;top:412px;width:120px;height:31px}
.service .map{left:528px;top:72px;width:607px;height:394px;background:var(--mint);border-radius:14px}

/* gallery */
.gallery-title{position:absolute;left:62px;top:3990px;font-size:40px;font-weight:700}
.tabs a{position:absolute;top:4008px;font-size:14px;color:var(--ink);text-decoration:none}
.tabs a.active{border-bottom:2px solid var(--teal);padding-bottom:3px}

/* contact */
.contact-panel{position:absolute;left:62px;top:4592px;width:495px;height:354px;background:linear-gradient(160deg,#4d5a52,#28332c);border-top-left-radius:70px}
.contact-panel h2{position:absolute;left:50px;top:92px;color:var(--white);font-size:40px;font-weight:600}
.contact-panel p{position:absolute;left:50px;top:162px;width:410px;color:var(--white);font-size:14px;line-height:22px}
.field{position:absolute;background:var(--card);border:1px solid var(--line);border-radius:4px;display:flex;align-items:center;gap:12px;padding-left:24px;font-size:12px;color:var(--muted)}
.field.message{align-items:flex-start;padding-top:12px}
.submit{left:613px;top:4915px;width:102px;height:33px}

/* footer */
.site-footer{position:absolute;left:0;top:5010px;width:1200px;height:295px;background:#f7f7f7;border-top:1px solid var(--line)}
.site-footer .tagline{position:absolute;left:60px;top:168px;width:260px;font-size:14px;line-height:22px}
.social{position:absolute;left:62px;top:218px;display:flex;gap:12px}
.social span{width:24px;height:24px;border-radius:50%;background:var(--teal)}
.fcol{position:absolute;top:40px}
.fcol h4{font-size:14px;font-weight:600;margin-bottom:14px}
.fcol li{list-style:none;font-size:14px;line-height:37px}
.fcol.contact{width:200px}
.fcol.contact li{line-height:22px;margin-bottom:12px}
.copyright{position:absolute;left:0;top:5305px;width:1200px;height:32px;background:var(--teal);color:var(--white);font-size:12px;display:flex;align-items:center;justify-content:center}
</style>
</head>
<body>

<header class="site-header">
  <div class="brand" style="left:62px;top:50px"><span class="mark"></span><span>Ridgecrest<br>Balusters</span></div>
  <nav class="nav">
    <a class="active" href="#" style="left:512px">Home</a>
    <a href="#" style="left:599px">About</a>
    <a href="#" style="left:684px">Products</a>
    <a href="#" style="left:790px">Services</a>
    <a href="#" style="left:893px">Gallery</a>
  </nav>
  <div class="btn btn-teal phone-btn">
    <svg width="14" height="14" viewBox="0 0 24 24" fill="#fff"><path d="M6.6 10.8a15.1 15.1 0 0 0 6.6 6.6l2.2-2.2c.3-.3.7-.4 1-.2 1.1.4 2.3.6 3.6.6.6 0 1 .4 1 1V20c0 .6-.4 1-1 1A17 17 0 0 1 3 4c0-.6.4-1 1-1h3.5c.6 0 1 .4 1 1 0 1.3.2 2.5.6 3.6.1.3 0 .7-.2 1z"/></svg>
    +123 555 0147
  </div>
</header>

<section class="hero">
  <div class="ph" role="img" aria-label="Concrete staircase with a metal handrail" style="left:830px;top:0;width:370px;height:555px;background:linear-gradient(180deg,#9c9e98,#6e706c 60%,#2a2c2a)"></div>
  <div class="hero-shadow"></div>
  <h1>Welcome to<br>RIDGECREST BALUSTERS</h1>
  <p>At Ridgecrest Balusters, we specialize in providing high-quality, stylish, and durable railing solutions for both residential and commercial properties. Whether you're looking to enhance the safety, functionality, or aesthetics of your space, our wide range of custom railings is designed to meet all your needs.</p>
  <div class="btn btn-white">Explore More</div>
</section>

<section class="about">
  <div class="credentials"><span class="accent">LICENSED</span>,<br>INSURED, &amp;<br>BONDED<br>WA GC LICENSE #<br>RIDGEBB802NS<br>Formed in 2020</div>
  <div class="about-label">About us</div>
  <div class="about-title">Building Trust, One<br>Railing at a Time</div>
  <div class="about-copy">
    <p>At <b>Ridgecrest Balusters</b>, we believe that every outdoor space deserves the perfect blend of style, safety, and durability. Serving homeowners, builders, and commercial developers across the Washington State, we specialize in crafting custom railing systems designed to withstand the region's unique climate while enhancing the beauty of your outdoor living spaces.</p>
    <p>With a focus on premium materials, expert craftsmanship, and exceptional customer service, <b>Ridgecrest Balusters</b> is proud to be the trusted partner for both residential and commercial railing projects. Whether you're looking to complement a new deck, add a modern touch to your balcony, or create a secure and stunning barrier for a commercial space, we've got the perfect solution for you.</p>
  </div>
  <div class="btn btn-teal" style="left:584px;top:1243px;width:125px;height:35px">Read More</div>
</section>

<section class="products">
  <div class="products-side"></div>
  <p class="products-intro">We offer a wide variety of custom and railing systems designed to meet the needs of every project:</p>
  <h2>Our Products</h2>
  <article class="product-card" style="left:52px">
    <div class="ph" role="img" aria-label="Aluminum railing on a modern balcony" style="background:linear-gradient(180deg,#5fb8c4,#b9c8cc)"></div>
    <h3>Aluminum Railings</h3>
    <p>For a sleek, low-maintenance option, our powder-coated aluminum .</p>
    <div class="btn btn-teal">Read More</div>
  </article>
  <article class="product-card" style="left:327px">
    <div class="ph" role="img" aria-label="Glass railing overlooking a city" style="background:linear-gradient(180deg,#c9d3d6,#7c8a88)"></div>
    <h3>Glass Railings</h3>
    <p>For a sleek, low-maintenance option, our powder-coated aluminum .</p>
    <div class="btn btn-teal">Read More</div>
  </article>
  <article class="product-card" style="left:603px">
    <div class="ph" role="img" aria-label="Cable railing on a deck" style="background:linear-gradient(180deg,#a9b1ad,#6d756f)"></div>
    <h3>Cable Railings</h3>
    <p>For a sleek, low-maintenance option, our powder-coated aluminum railings.</p>
    <div class="btn btn-teal">Read More</div>
  </article>
  <article class="product-card" style="left:878px">
    <div class="ph" role="img" aria-label="Custom wrought metal railing against the sea" style="background:linear-gradient(180deg,#3a8fd0,#1d3b5a)"></div>
    <h3>Custom</h3>
    <p>For a sleek, low-maintenance option, our powder-coated aluminum railings .</p>
    <div class="btn btn-teal">Read More</div>
  </article>
  <div class="dots"><span></span><span></span><span></span><span></span></div>
</section>

<section class="why">
  <h2 class="why-title">Why Choose<br>Ridgecrest Balusters ?</h2>
  <div class="ph" role="img" aria-label="House with glass balcony railings" style="left:64px;top:2157px;width:236px;height:313px;background:linear-gradient(180deg,#6c7570,#3b403d);border-top-left-radius:40px"></div>
  <div class="ph" role="img" aria-label="Smiling installer in a hard hat and safety vest" style="left:311px;top:2157px;width:234px;height:429px;background:linear-gradient(180deg,#00bba5,#00ab8e)"></div>
  <div class="ph" role="img" aria-label="Exterior stair with black railing" style="left:64px;top:2486px;width:236px;height:293px;background:linear-gradient(180deg,#8a8f8c,#4c514e);border-bottom-left-radius:40px"></div>
  <div class="ph" role="img" aria-label="Modern house with deck railing" style="left:311px;top:2602px;width:234px;height:177px;background:linear-gradient(180deg,#b8bcb9,#4a4e4b);border-bottom-right-radius:40px"></div>

  <div class="feature" style="left:584px;top:2147px">
    <div class="num">1</div>
    <h3 style="top:80px">Locally Crafted, Regionally Resilient</h3>
    <p style="top:150px">Our railings are designed with the Pacific Northwest's weather in mind—rain, snow, and everything in between. We use durable materials that are resistant to corrosion, moisture.</p>
  </div>
  <div class="feature" style="left:866px;top:2147px;border-top-right-radius:90px">
    <div class="num">2</div>
    <h3>Custom Solutions for Every Need</h3>
    <p style="top:140px">We work closely with you to design and fabricate custom railing systems that perfectly suit your space, style, and functional requirements. From intricate designs to minimalistic finishes.</p>
  </div>
  <div class="feature" style="left:584px;top:2474px">
    <div class="num">3</div>
    <h3>Full-Service Partner</h3>
    <p style="top:140px">Our skilled craftsmen take pride in delivering exceptional workmanship, while our professional installers ensure every railing is securely mounted.</p>
  </div>
  <div class="feature" style="left:866px;top:2474px">
    <div class="num">4</div>
    <h3>Expert Installation &amp; Craftsmanship</h3>
    <p style="top:140px">Our railings are designed with the Pacific Northwest's weather in mind—rain, snow, and everything in between. We use durable materials that are resistant to corrosion, moisture.</p>
  </div>
</section>

<section class="process">
  <h2 class="process-title">Our Process</h2>
  <article class="process-card" style="left:56px">
    <div class="ph" role="img" aria-label="Team reviewing drawings on a desk" style="background:linear-gradient(160deg,#c99a6a,#e8e2d8)"></div>
    <div class="icon-box"><svg width="44" height="44" viewBox="0 0 44 44" fill="none" stroke="#00ab8e" stroke-width="2"><rect x="6" y="6" width="32" height="32" rx="3"/><path d="M12 30 30 12M12 22h10M22 12v10"/></svg></div>
    <h3>Professional Installation</h3>
    <p>Our experienced team handles all aspects of installation, from measuring to securing.</p>
    <div class="btn btn-teal">Read More</div>
  </article>
  <article class="process-card" style="left:425px">
    <div class="ph" role="img" aria-label="Wooden blocks with support symbols" style="background:linear-gradient(180deg,#f2eee9,#c9a98a)"></div>
    <div class="icon-box"><svg width="44" height="44" viewBox="0 0 44 44" fill="none" stroke="#00ab8e" stroke-width="2"><circle cx="22" cy="22" r="14"/><circle cx="22" cy="22" r="6"/></svg></div>
    <h3>Ongoing Support</h3>
    <p>We offer warranties on all of our products and services, and we are always available to help with maintenance.</p>
    <div class="btn btn-teal">Read More</div>
  </article>
  <article class="process-card" style="left:796px">
    <div class="ph" role="img" aria-label="Team reviewing drawings on a desk" style="background:linear-gradient(160deg,#c99a6a,#e8e2d8)"></div>
    <div class="icon-box"><svg width="44" height="44" viewBox="0 0 44 44" fill="none" stroke="#00ab8e" stroke-width="2"><rect x="6" y="6" width="32" height="32" rx="3"/><path d="M12 30 30 12M12 22h10M22 12v10"/></svg></div>
    <h3>Consultation &amp; Design</h3>
    <p>We start by listening to your vision and understanding your specific needs. Our team will offer expert advice</p>
    <div class="btn btn-teal">Read More</div>
  </article>
</section>

<section class="service" role="img" aria-label="Coastal cliffs under a cloudy sky">
  <h2>Serving<br>Washington State</h2>
  <p>Ridgecrest Balusters is proud to serve the entire state of Washington. Whether you're upgrading your home's deck or outfitting a commercial space, we understand the importance of creating beautiful, durable railings that stand up to the region's diverse and often challenging weather conditions.</p>
  <div class="btn btn-teal">Book Now</div>
  <div class="ph map" role="img" aria-label="Map of Washington State"></div>
</section>

<section class="gallery">
  <h2 class="gallery-title">Gallery</h2>
  <div class="tabs">
    <a class="active" href="#" style="left:814px">Railing Project Pictures</a>
    <a href="#" style="left:1009px">Remodel Projects</a>
  </div>
  <div class="ph" role="img" aria-label="Interior black metal railing" style="left:62px;top:4078px;width:456px;height:209px;background:linear-gradient(180deg,#f0efec,#c8b9a8);border-top-left-radius:50px"></div>
  <div class="ph" role="img" aria-label="Deck with railing overlooking trees" style="left:549px;top:4078px;width:271px;height:209px;background:linear-gradient(180deg,#b9c4cc,#4f5a54)"></div>
  <div class="ph" role="img" aria-label="Multi-level home with balcony railings" style="left:854px;top:4078px;width:283px;height:209px;background:linear-gradient(180deg,#c7cdd2,#6a5e52)"></div>
  <div class="ph" role="img" aria-label="Railing in front of forest" style="left:62px;top:4314px;width:269px;height:209px;background:linear-gradient(180deg,#6f7a6e,#2e3a30)"></div>
  <div class="ph" role="img" aria-label="Grey house with horizontal rail balcony" style="left:363px;top:4314px;width:457px;height:209px;background:linear-gradient(180deg,#7d8180,#3d4140)"></div>
  <div class="ph" role="img" aria-label="Stair railing under construction" style="left:854px;top:4314px;width:283px;height:209px;background:linear-gradient(180deg,#b2755a,#c9c9c5);border-bottom-right-radius:50px"></div>
</section>

<section class="contact">
  <div class="contact-panel" role="img" aria-label="Railing set against evergreen trees">
    <h2>Contact Us Today</h2>
    <p>Ready To Elevate Your Space With A Custom Railing Solution That's Built To Last? Reach Out To The Ridgecrest Balusters Team For A Free Consultation. Let Us Bring Your Vision To Life With Craftsmanship, Care, And Precision.</p>
  </div>
  <div class="field" style="left:613px;top:4590px;width:522px;height:45px">
    <svg width="18" height="18" viewBox="0 0 24 24" fill="none" stroke="#999" stroke-width="1.6"><circle cx="12" cy="8" r="4"/><path d="M4 21c0-4 4-6 8-6s8 2 8 6"/></svg>Name*</div>
  <div class="field" style="left:613px;top:4656px;width:251px;height:47px">
    <svg width="18" height="18" viewBox="0 0 24 24" fill="none" stroke="#999" stroke-width="1.6"><rect x="3" y="5" width="18" height="14" rx="2"/><path d="m3 7 9 6 9-6"/></svg>Email*</div>
  <div class="field" style="left:883px;top:4656px;width:252px;height:47px">
    <svg width="18" height="18" viewBox="0 0 24 24" fill="none" stroke="#999" stroke-width="1.6"><path d="M6.6 10.8a15 15 0 0 0 6.6 6.6l2.2-2.2 4.6 1.4V20A17 17 0 0 1 3 4h3.5l1.4 4.6z"/></svg>Number*</div>
  <div class="field" style="left:613px;top:4724px;width:522px;height:48px">
    <svg width="18" height="18" viewBox="0 0 24 24" fill="none" stroke="#999" stroke-width="1.6"><path d="M3 12V4h8l10 10-8 8z"/><circle cx="7.5" cy="8.5" r="1.5"/></svg>Subject*</div>
  <div class="field message" style="left:613px;top:4791px;width:522px;height:103px">Message*</div>
  <div class="btn btn-teal submit">Submit</div>
</section>

<footer class="site-footer">
  <div class="brand" style="left:62px;top:52px"><span class="mark"></span><span>Ridgecrest<br>Balusters</span></div>
  <p class="tagline">Durable, Stylish, And Built For The Pacific Northwest.</p>
  <div class="social"><span></span><span></span><span></span><span></span></div>
  <div class="fcol" style="left:427px"><h4>Information</h4><ul><li>Home</li><li>About Us</li><li>Services</li><li>Our Products</li><li>Contact Us</li></ul></div>
  <div class="fcol" style="left:698px"><h4>Resources</h4><ul><li>Terms Of Condition</li><li>Privacy Policy</li><li>Cookies</li></ul></div>
  <div class="fcol contact" style="left:974px"><h4>Quick Contact</h4><ul><li>Lorem Ipsum Dolor<br>Sit Amet,<br>Consectetur<br>Adipiscing Elit.</li><li>info@ridgecrest.example</li><li>123-555-0147</li></ul></div>
</footer>
<div class="copyright">2024 Copyright ©Ridgecrest Balusters Inc All Rights Reserved</div>

</body>
</html>
```